Home page web design for a lawn specialist business

-The design must be based around the attached HPID (home page information design) called Turf Tidings HPID. I've attached Word and PDF versions - these are the same. The table boxes are just for approximate placement of information and you can use boxes and bold shapes for this design.

All fonts used in the HPID are only examples - you can use any Google font you wish.

- Text that is in orange is for your information only. Text to go on the design is black. Some instructions are in the HPID. Please be creative!

-The design needs to be modern and exciting - colours are to be the green of the logo, and white ...and then choose dark green, or dark grey or black.

Logo - attached (it's not great quality but don't worry, we'll replace it later)

- I've provided the images for the galleries - they are labelled and will match the name in the HPID. Please use the supplied images!

- Examples of some websites that have great design... don't copy them please but they are similar in look to what we are after....
www.qmbbuildworks.co.nz
http://www.rim-safeguard.co.nz/
http://www.lumenhomes.wb.gs/

Important: Width of content will be 1280 pixels when implemented as a web page but the winning design will need to supplied be on a 2000 pixel wide background so nav bars and background can extend outside the 1280 width.
Header height (without nav bar) 150-160 pixels.

We don't comment on individual designs but will choose a winning design promptly.

Industry/Entity Type

Business

Number of Pages Required

1 page

Font styles to use
Sans Serif

Requirements
Must have
• clean, modern, well-spaced design

```html
<!DOCTYPE html>
<html lang="en">
<head>
<meta charset="utf-8">
<title>Turf Tidings – Lawn Specialists</title>
<link href="https://fonts.googleapis.com/css2?family=Open+Sans:ital,wght@0,400;0,600;0,700;1,400&display=swap" rel="stylesheet">
<style>
:root{
  --green:#3a9b2f;
  --green-dark:#2c7f23;
  --ink:#1f1f1f;
  --text:#555;
  --grey:#ebebeb;
  --white:#fff;
  --line:#d8d8d8;
}
*{box-sizing:border-box;margin:0;padding:0}
html,body{width:673px;height:1200px;overflow:hidden}
body{font-family:'Open Sans',Arial,sans-serif;background:var(--white);color:var(--text);position:relative}
.wrap{position:absolute;left:97px;width:478px}
.band{position:absolute;left:0;width:673px}

/* header */
.header{top:0;height:59px}
.brand{position:absolute;left:0;top:12px;display:flex;align-items:center;gap:6px}
.brand-mark{width:30px;height:30px;background:var(--green)}
.brand-name{font-size:15px;font-weight:700;color:var(--green)}
.contact{position:absolute;right:0;top:7px;text-align:left;width:128px}
.contact h3{font-size:10px;font-weight:700;color:var(--ink);letter-spacing:.3px}
.contact p{font-size:5.5px;color:var(--text);line-height:1.3}
.contact .region{text-align:right}
.phone-row{display:flex;align-items:center;gap:6px;margin-top:-2px}
.phone-row span{font-size:13px;font-weight:700;color:var(--green)}

/* nav */
.nav{top:59px;height:19px;background:var(--green)}
.nav ul{list-style:none;display:flex;height:19px}
.nav li{font-size:5px;font-weight:600;color:var(--white);line-height:19px;padding:0 7.2px;text-transform:uppercase}
.nav li.active{background:var(--ink)}

/* slider */
.slider-bg{top:78px;height:160px;background:var(--grey)}
.slider{position:absolute;top:0;height:160px;display:flex;box-shadow:0 6px 6px -3px rgba(0,0,0,.35)}
.slide{width:239px;height:160px}
.slide.before{background:linear-gradient(180deg,#d9d6cf 0%,#b4a89a 35%,#6b5444 100%)}
.slide.after{background:linear-gradient(180deg,#d8d8d0 0%,#8bbf5a 35%,#3f8f26 100%)}
.caption{position:absolute;font-size:12.5px;font-weight:700;color:var(--white);padding:5px 8px;letter-spacing:.2px}
.caption.before{left:92px;top:61px;background:rgba(25,25,25,.88)}
.caption.after{left:242px;top:70px;background:rgba(58,155,47,.92)}
.arrow{position:absolute;top:72px;width:13px;height:14px;background:var(--green);display:flex;align-items:center;justify-content:center}
.arrow.prev{left:4px}.arrow.next{right:4px}

/* intro */
.intro{top:255px;text-align:center}
.intro h1{font-size:14px;font-weight:400;color:var(--green)}
.intro h2{font-size:9.5px;font-weight:400;color:var(--ink);margin-top:1px}
.dots{width:254px;margin:8px auto 10px;border-top:1px dotted #8aa;}
.intro p{font-size:5.8px;line-height:1.55;margin-bottom:8px}

/* services */
.services-bg{top:369px;height:351px;background:var(--grey)}
.card{position:absolute;width:235px;height:153px;background:var(--white);box-shadow:0 4px 5px -2px rgba(0,0,0,.25)}
.card .photo{position:absolute;left:3px;top:3px;width:229px;height:80px}
.card .icon{position:absolute;right:5px;top:54px;width:46px;height:46px;border-radius:50%;background:var(--white);border:2px solid var(--green);display:flex;align-items:center;justify-content:center}
.card .icon i{width:36px;height:36px;border-radius:50%;background:var(--green);display:flex;align-items:center;justify-content:center}
.card h4{position:absolute;left:7px;top:92px;font-size:7px;font-weight:700;color:var(--ink);text-transform:uppercase;letter-spacing:.2px}
.card .rule{position:absolute;left:7px;right:8px;top:105px;border-top:1px solid var(--line)}
.card p{position:absolute;left:7px;right:20px;top:110px;font-size:5px;line-height:1.5}
.btn{display:inline-block;background:var(--green);color:var(--white);font-size:4.4px;font-weight:600;text-transform:uppercase;padding:3px 5px}
.card .btn{position:absolute;left:7px;top:133px}
.photo.seed{background:linear-gradient(180deg,#4e5a3e 0%,#6f8f5d 40%,#3f8d8d 70%,#2f7a7a 100%)}
.photo.care{background:linear-gradient(180deg,#cfd9c8 0%,#7fb54a 40%,#3f8d24 100%)}
.photo.faq{background:linear-gradient(180deg,#bdb7a8 0%,#8fa96b 40%,#4c9a2a 100%)}
.photo.gallery{background:linear-gradient(90deg,#5f8a8a 0%,#4c8686 50%,#7fae57 50%,#4a9430 100%)}

/* video */
.video{top:742px}
.video h5{font-size:7px;font-weight:600;color:var(--ink);width:270px;line-height:1.25}
.player{position:absolute;top:27px;left:0;width:278px;height:94px;background:linear-gradient(180deg,#6c7680 0%,#8aa56a 45%,#4d962b 100%);border:3px solid var(--white);box-shadow:0 5px 5px -3px rgba(0,0,0,.35)}
.play{position:absolute;left:117px;top:27px;text-align:center;color:var(--white);font-size:6.5px;font-weight:700}
.play svg{display:block;margin:0 auto 1px}
.about{position:absolute;left:299px;top:0;width:180px}
.about h3{font-size:10px;font-weight:700;color:var(--ink)}
.about h3 span{color:var(--green)}
.about .rule{border-top:1px solid var(--line);margin:4px 0 8px}
.about p{font-size:5px;line-height:1.5;margin-bottom:6px}
.about .btn{font-size:5px;padding:4px 7px;margin-top:2px}

/* testimonial */
.testimonial-bg{top:890px;height:120px;background:var(--grey)}
.testimonial{top:903px}
.testimonial h5{font-size:6px;font-weight:700;color:var(--ink);width:200px;line-height:1.3;text-transform:uppercase}
.quote{position:absolute;top:20px;left:0;width:234px;height:48px;background:var(--green);color:var(--white);font-size:5.5px;font-style:italic;line-height:1.6;padding:14px 10px 0 24px}
.quote b{position:absolute;left:12px;top:4px;font-size:14px;font-style:normal}
.quote::after{content:"";position:absolute;left:30px;bottom:-6px;border-left:6px solid transparent;border-right:6px solid transparent;border-top:6px solid var(--green)}
.author{position:absolute;top:80px;left:174px;text-align:right;width:40px}
.author strong{display:block;font-size:5.5px;color:var(--ink);font-weight:600;white-space:nowrap}
.author span{display:block;font-size:4.5px;white-space:nowrap}
.mower{position:absolute;left:244px;top:13px;width:234px;height:80px;background:linear-gradient(180deg,#a9c48a 0%,#6ea93c 40%,#3f8d24 100%)}

/* footer */
.footer{top:1032px}
.col{position:absolute;top:0}
.col h6{font-size:6.2px;font-weight:600;color:var(--ink);padding-bottom:4px;border-bottom:1px solid var(--line);margin-bottom:6px}
.col p{font-size:4.6px;line-height:1.6}
.col ul{list-style:none;font-size:4.6px;line-height:1.62}
.col li.active{color:var(--green)}
.foot-brand{display:flex;align-items:center;gap:4px;margin-bottom:8px}
.foot-brand i{width:20px;height:20px;background:var(--green)}
.foot-brand span{font-size:10px;font-weight:700;color:var(--green)}
.badge{width:70px;height:70px;border-radius:50%;background:#9bc95a;margin:2px 0 0 6px}
.quote-form{position:absolute;left:299px;top:0;width:180px}
.quote-form h6{font-size:5px;font-weight:600;color:var(--ink);line-height:1.4;margin-bottom:6px}
.quote-form h6 span{color:var(--green)}
.fields{display:grid;grid-template-columns:1fr 1fr;gap:5px}
.field{height:14px;background:#f0f0f0;font-size:4px;color:#999;padding:4px 6px}
.field.area{grid-column:1/3;height:37px}
.quote-form .btn{margin-top:5px;font-size:5px;padding:4px 7px}

/* bottom */
.grass{top:1155px;height:27px;background:linear-gradient(180deg,#fff 0%,#7cc45a 45%,#3a9b2f 100%)}
.bottom{top:1180px;height:20px;background:var(--green)}
.bottom .wrap{top:0;height:20px;display:flex;justify-content:space-between;align-items:center;font-size:4px;color:var(--white)}
.social{display:flex;align-items:center;gap:4px}
.social i{width:9px;height:9px;border-radius:50%;background:rgba(255,255,255,.35)}
</style>
</head>
<body>

<header class="band header">
  <div class="wrap" style="top:0;height:59px">
    <div class="brand"><span class="brand-mark"></span><span class="brand-name">Turf Tidings</span></div>
    <div class="contact">
      <h3>LAWN SPECIALISTS</h3>
      <p>from ground preparation to lawn aftercare</p>
      <p class="region">SERVICING THE AUCKLAND REGION</p>
      <div class="phone-row">
        <svg width="18" height="14" viewBox="0 0 18 14"><path d="M1 4c0-2 3-3 8-3s8 1 8 3v2h-4V4.5H5V6H1z" fill="#1f1f1f"/><path d="M4 7h10l2 6H2z" fill="#1f1f1f"/><circle cx="9" cy="10" r="2" fill="#fff"/></svg>
        <span>0800 40 21 63</span>
      </div>
    </div>
  </div>
</header>

<nav class="band nav">
  <div class="wrap" style="top:0">
    <ul>
      <li class="active">Home</li><li>About Us</li><li>Services</li><li>Lawn Care</li><li>Seasonal Care</li><li>Hydroseeding</li><li>FAQs</li><li>Before &amp; After</li><li>Gallery</li><li>Quote / Contact</li>
    </ul>
  </div>
</nav>

<section class="band slider-bg">
  <div class="wrap slider">
    <div class="slide before" role="img" aria-label="Bare prepared soil before grass seeding"></div>
    <div class="slide after" role="img" aria-label="Lush green lawn after grass seeding"></div>
    <div class="caption before">Befor Grass Seeding</div>
    <div class="caption after">After Grass Seeding</div>
    <div class="arrow prev"><svg width="5" height="6"><path d="M4 0L1 3l3 3" stroke="#fff" fill="none"/></svg></div>
    <div class="arrow next"><svg width="5" height="6"><path d="M1 0l3 3-3 3" stroke="#fff" fill="none"/></svg></div>
  </div>
</section>

<section class="wrap intro">
  <h1>You can always spot an Turf Tidings lawn</h1>
  <h2>It's the one that turns your neighbours green with envy.</h2>
  <div class="dots"></div>
  <p>If you want a lawn or playing field that looks good throughout the year, talk to us. Turf Tidings are New Zealand's experts in high quality grass seeding and lawn maintenance, creating the lushest lawns you'll ever see. With high-tech equipment, years of experience and expert aftercare, nobody knows grass like Turf Tidings.</p>
  <p>There are many factors that influence the quality of a lawn, including seasonality, growing conditions, shade, seed types, and time. A one-size-fits-all solution couldn't possibly guarantee a great lawn, so we provide personalised advice, a full range of seeding techniques</p>
</section>

<section class="band services-bg">
  <div class="wrap" style="top:0;height:351px">
    <article class="card" style="left:1px;top:17px">
      <div class="photo seed" role="img" aria-label="Freshly hydroseeded garden bed"></div>
      <div class="icon"><i><svg width="20" height="20" viewBox="0 0 20 20" fill="#fff"><path d="M3 18C4 12 3 8 2 5c3 3 4 7 4 13zM8 18c0-6 1-11 3-15-1 5-1 10 0 15zM12 18c1-5 3-9 6-11-2 3-3 7-3 11z"/></svg></i></div>
      <h4>Grass Seeding Services</h4><div class="rule"></div>
      <p>With a wide range of grass seed applications to choose from, including hydroseeding and instant lawn, there is an option to suit your property and your requirements.</p>
      <span class="btn">More about grass seeding</span>
    </article>
    <article class="card" style="left:244px;top:17px">
      <div class="photo care" role="img" aria-label="Sprinkler watering a green lawn"></div>
      <div class="icon"><i><svg width="20" height="20" viewBox="0 0 20 20" fill="none" stroke="#fff" stroke-width="1.5"><path d="M4 9h8v6H4zM12 11l5-4M4 11L2 9"/><path d="M7 18c0-2 1-3 3-3"/></svg></i></div>
      <h4>Lawn Care Maintenance</h4><div class="rule"></div>
      <p>As well as lawn care services, the team at Turf Tidings provides helpful information for regular upkeep of your residential or commercial lawn.</p>
      <span class="btn">More about ongoing lawn care</span>
    </article>
    <article class="card" style="left:1px;top:179px">
      <div class="photo faq" role="img" aria-label="Raised lawn bed with a tree"></div>
      <div class="icon"><i><svg width="20" height="20" viewBox="0 0 20 20"><path d="M3 3h14v11H9l-4 4v-4H3z" fill="#fff"/><text x="10" y="12.5" font-size="10" font-weight="700" text-anchor="middle" fill="#3a9b2f" font-family="Open Sans,sans-serif">?</text></svg></i></div>
      <h4>FAQs about grass seeding and lawn care</h4><div class="rule"></div>
      <p>For more information, read our frequently asked questions regarding grass seeding and lawn care.</p>
      <span class="btn">Grass seeding &amp; lawn care FAQs</span>
    </article>
    <article class="card" style="left:244px;top:179px">
      <div class="photo gallery" role="img" aria-label="Before and after views of a new lawn"></div>
      <div class="icon"><i><svg width="20" height="20" viewBox="0 0 20 20" fill="none" stroke="#fff" stroke-width="1.5"><rect x="5" y="4" width="12" height="10"/><path d="M3 7v10h11"/><path d="M6 13l4-4 3 3 2-2 2 2"/></svg></i></div>
      <h4>Before and after lawn photos</h4><div class="rule"></div>
      <p>See what you potential new lawn could look like by viewing a range of before and after lawn seeding photos.</p>
      <span class="btn">Before and after photos</span>
    </article>
  </div>
</section>

<section class="wrap video">
  <h5>Watch the video on how Turf Tidings can transform your empty spaces into beautiful green grass lawns.</h5>
  <div class="player" role="img" aria-label="Video still of a finished front lawn">
    <div class="play"><svg width="28" height="20" viewBox="0 0 28 20"><rect width="28" height="20" rx="3" fill="#fff" opacity=".9"/><path d="M11 5l8 5-8 5z" fill="#555"/></svg>PLAY VIDEO</div>
  </div>
  <div class="about">
    <h3>Turf <span>Tidings..</span></h3>
    <div class="rule"></div>
    <p>For all things grass, you need the best! Turf Tidings are skilled specialists when it comes to creating the perfect lawn for your property.</p>
    <p>From pre-seeding preparation to a full range of grass seeding services and lawn after care options, you'll enjoy a healthy green lawn for many years.</p>
    <p>Selling your property? Turf Tidings will add the wow factor to the outdoor areas of your home with a lush green lawn.</p>
    <span class="btn">Find out more</span>
  </div>
</section>

<section class="band testimonial-bg"></section>
<section class="wrap testimonial">
  <h5>"I would recommend Turf Tidings to anyone who wants an amazing lawn"</h5>
  <div class="quote"><b>“</b>Testimonial here about how great Turf Tidings were to deal with and how they are so happy with the lawn and the after care services etc etc.</div>
  <div class="author"><strong>Ravi Moana</strong><span>Homeowner, Kerrvale</span></div>
  <div class="mower" role="img" aria-label="Lawn mower cutting a green lawn"></div>
</section>

<footer class="wrap footer">
  <div class="col" style="left:0;width:105px">
    <h6>Company Info</h6>
    <div class="foot-brand"><i></i><span>Turf Tidings</span></div>
    <p>Contrary to popular belief, Lorem Ipsum is not simply random text. It has roots in a piece of classical Latin literature from 45 BC, making it over 2000 years old.</p>
  </div>
  <div class="col" style="left:116px;width:78px">
    <h6>Navigation</h6>
    <ul><li class="active">Home</li><li>About us</li><li>Services</li><li>Lawn care</li><li>Seasonal care</li><li>Hydroseeding</li><li>FAQs</li><li>Before &amp; After Gallery</li><li>Quote / Contact</li></ul>
  </div>
  <div class="col" style="left:204px;width:80px">
    <h6 style="border:0">Diploma In Horticulture</h6>
    <div class="badge"></div>
  </div>
  <div class="quote-form">
    <h6>Get a quote for your new lawn!<br>Fill in the form or phone us on <span>0800 40 21 63.</span></h6>
    <div class="fields">
      <div class="field">First Name</div><div class="field">First Name</div>
      <div class="field">First Name</div><div class="field">First Name</div>
      <div class="field area"></div>
    </div>
    <span class="btn">Call me back</span>
  </div>
</footer>

<div class="band grass" role="img" aria-label="Strip of grass blades"></div>
<div class="band bottom">
  <div class="wrap">
    <span>© 2014 Turf Tidings. All right reserved. Term of Use</span>
    <span class="social">Follow us <i></i><i></i><i></i></span>
  </div>
</div>

</body>
</html>
```